International Petrochemical business needs a web design for Tessaro Desk system

We need a web design for a "Tessaro Desk" system for an international petrochemical company. The web site is used internally within the company. It is hosted by an internal department which provides government permit request service for other departments.

We would like to see designs of two pages using color light blue. (home page, internal page as attached).
Home Page:
1. Header has a background image and small animation. Header on home page can be taller than the header of the internal page.
2. Layout as attached.

Internal Page:
1. Header can use the same background image as the home page and can be shorter to utilize the page for content.
2. The blue icon behind every captions represent an icon. When user move mouse over this icon, it displays the caption in Thai language as a tooltip. This icon needs to be redesign.

The final design should communicate the followings:
- Excellent service provided system in terms of time and accurary
- Rapid growth of business via building petrochemical refinery plant

For Internal Page, the blue circle behind every captions represent an icon. When mouse over this icon, a tool tip showing the caption in Thai language is shown. Please also design this icon..

There are more feedbacks from customer as followed:

1. Banner should consists of 
    1.1 "Approved" stamp on paper
    1.2 An image of Garuda. It is used on every government documents in Thailand
    1.3 Image of petrochemical plant
2. Each menu item (Home, Permit, Search, etc) should have different colors. Drop down menu will use the same color as its parent menu item.
3. Overall tone of the web page should be light blue with background of the body the web page in white
4. "New Request" button should use green color with icon on it
5. Table header of each box in the body of the page should use dark blue background with text in white

Please kindly submit your revisions.
Thank you.

Reason: We get some late feedbacks from customers which was just updated to all designers.

• 1. Design for 1024x768 screen resolution
2. Use light blue theme
3. Background of header where the company logo is must have white background

```html
<!DOCTYPE html>
<html lang="en">
<head>
<meta charset="utf-8">
<title>Tessaro Desk System</title>
<link href="https://fonts.googleapis.com/css2?family=Cabin:wght@400;500;600;700&display=swap" rel="stylesheet">
<style>
:root{
  --sky:#c9ecfb;
  --panel-line:#9fd0ea;
  --title-blue:#1b86c8;
  --link-blue:#2f8fcf;
  --navy:#14285f;
  --ink:#333a40;
  --red:#e3212b;
  --pager:#2d5ca8;
  --band:#0b89c5;
  --cta:#15a6df;
  --white:#ffffff;
}
*{box-sizing:border-box;margin:0;padding:0}
html,body{width:1200px;height:1172px;overflow:hidden}
body{font-family:"Cabin",sans-serif;color:var(--ink);background:var(--sky);position:relative}
.abs{position:absolute}

/* header */
.brand{left:26px;top:42px;font-size:24px;font-weight:600;color:var(--link-blue);line-height:28px;white-space:nowrap}
.system-title{right:22px;top:14px;font-size:24px;font-weight:700;color:var(--navy);letter-spacing:.5px}
.nav{left:276px;top:66px;width:902px;height:48px;background:var(--white);border-radius:6px 6px 0 0;display:flex;align-items:center;padding-left:4px}
.nav-item{font-size:16px;font-weight:500;color:var(--title-blue);padding:0 22px;height:48px;line-height:48px;border-right:1px solid #e0eef6}
.nav-item.is-active{color:var(--red);padding:0 30px}
.nav-item:last-of-type{border-right:none}
.search{position:absolute;left:664px;top:12px;width:218px;height:28px;border:1px solid var(--navy);display:flex;align-items:center;padding-left:40px;font-size:12px;font-style:italic;color:#777}
.search svg{position:absolute;right:4px;top:3px}

/* banner */
.banner{left:22px;top:114px;width:1156px;height:244px;background:linear-gradient(90deg,#8fb3d6 0%,#5a7fb8 30%,#47539c 55%,#3b4a92 100%)}
.banner-title{left:704px;top:170px;font-size:30px;font-weight:600;color:var(--white)}
.banner-text{left:704px;top:224px;width:300px;font-size:16px;font-weight:600;line-height:22px;color:var(--white)}
.slider{left:1012px;top:302px;width:177px;height:31px;background:var(--white);border-radius:4px;display:flex;align-items:center;justify-content:center;gap:14px}
.slider i{width:15px;height:15px;border-radius:50%;background:var(--pager)}
.slider i.is-current{background:var(--red)}
.dropdown{left:395px;top:114px;width:232px;height:130px;background:rgba(230,236,244,.92);border-bottom:3px solid var(--red);padding:6px 0 0 40px}
.dropdown li{list-style:none;font-size:14px;font-weight:500;color:#222;line-height:24px}
.dropdown li.is-current{position:relative}
.dropdown li.is-current::before{content:"";position:absolute;left:-14px;top:8px;border-left:7px solid var(--link-blue);border-top:4px solid transparent;border-bottom:4px solid transparent}

/* content */
.content{left:22px;top:358px;width:1156px;height:649px;background:var(--white)}
.panel{border:1px solid var(--panel-line);border-radius:8px;background:var(--white);overflow:hidden}
.panel::before{content:"";position:absolute;left:0;top:0;right:0;height:58px;background:linear-gradient(#d6edf9,#ffffff)}
.panel-title{position:absolute;left:20px;top:8px;font-size:19px;font-weight:500;color:var(--title-blue)}
.panel-icon{position:absolute}
.th,.td{position:absolute;display:grid}
.th span{font-size:14.5px;font-weight:600;color:#3c3c3c;line-height:18px}
.td{grid-auto-rows:23px}
.td span{font-size:14.5px;line-height:23px;color:var(--ink);white-space:nowrap;display:flex;align-items:center;gap:6px}
.td a{color:var(--link-blue);text-decoration:none}
.pager{position:absolute;width:105px;height:23px;background:var(--pager);border-radius:7px;display:flex;align-items:center;justify-content:center;gap:7px;font-size:12px;font-weight:700;color:var(--white)}
.pager b{color:var(--red);font-weight:700}
.flag{width:16px;height:16px;border-radius:50%}
.flag.is-red{background:radial-gradient(circle at 40% 35%,#ff8a8a,#e3212b)}
.flag.is-amber{background:radial-gradient(circle at 40% 35%,#fff0a8,#f0c542)}

.faq{left:917px;top:373px;width:248px;height:389px;border:1px solid var(--panel-line);border-radius:8px;background:var(--white)}
.faq-inner{position:absolute;left:9px;top:11px;width:227px;height:364px;background:var(--sky);border-radius:3px}
.faq-title{position:absolute;left:10px;top:14px;font-size:26px;font-weight:600;line-height:32px;color:var(--title-blue)}
.faq-list{position:absolute;left:17px;top:104px;list-style:none}
.faq-list li{font-size:14px;font-weight:600;color:var(--navy);line-height:24px}
.faq-list li::before{content:"›";color:var(--link-blue);font-weight:700;margin-right:8px}
.faq-help{position:absolute;left:113px;top:311px;width:99px;height:28px;border-radius:5px;background:linear-gradient(#ff4a55,#d8101c);color:var(--white);font-size:13px;font-weight:600;text-align:center;line-height:28px}

.cta{left:485px;top:784px;width:417px;height:45px;background:var(--cta);border-radius:3px;color:var(--white);font-size:19px;font-weight:600;padding-left:19px;line-height:45px}
.cta::after{content:"";display:inline-block;margin-left:18px;border-left:11px solid var(--white);border-top:6px solid transparent;border-bottom:6px solid transparent}

/* footer */
.footer-band{left:0;top:1022px;width:1200px;height:150px;background:var(--band)}
.footer-media{left:235px;top:1057px;width:709px;height:73px;background:linear-gradient(90deg,#0b2f8f 0%,#1f5fcf 45%,#b8d6f2 70%,#cfe3f6 100%);display:flex;align-items:center;justify-content:flex-end;padding-right:115px;font-size:15px;color:#23324f}
.footer-text{left:0;top:1140px;width:1200px;text-align:center;font-size:15px;color:var(--white)}
</style>
</head>
<body>

<header>
  <div class="abs brand">Norvane Chemical</div>
  <div class="abs system-title">TESSARO DESK SYSTEM</div>
  <nav class="abs nav">
    <span class="nav-item is-active">HOME</span>
    <span class="nav-item">PERMITS</span>
    <span class="nav-item">SEARCH</span>
    <span class="nav-item">REPORT</span>
    <span class="nav-item">ADMIN</span>
    <span class="nav-item">HELP</span>
    <div class="search">Keyword Search
      <svg width="22" height="22" viewBox="0 0 22 22"><circle cx="9" cy="9" r="6.5" fill="#8fd3f3" stroke="#1b86c8" stroke-width="2.5"/><path d="M13.5 13.5 20 20" stroke="#1b86c8" stroke-width="3.5" stroke-linecap="round"/></svg>
    </div>
  </nav>
</header>

<section class="abs banner" role="img" aria-label="Photograph of steel petrochemical plant pipework against a blue sky"></section>
<div class="abs banner-title">Lorem ipsum dolor sit amet</div>
<p class="abs banner-text">Consectetur adipisicing elit, sed do eiusmod tempor incididunt ut labore et dolore magna aliqua.</p>
<div class="abs slider"><i></i><i class="is-current"></i><i></i><i></i><i></i></div>

<ul class="abs dropdown">
  <li class="is-current">Lorem ipsum dolor sit</li>
  <li>Pamet, consectetur</li>
  <li>Ladipisicing elit, sed do</li>
  <li>Heiusmod tempor</li>
  <li>Kincididunt ut labore et</li>
</ul>

<main>
  <div class="abs content"></div>

  <section class="abs panel" style="left:41px;top:375px;width:424px;height:218px">
    <h2 class="panel-title">New Requests</h2>
    <svg class="panel-icon" style="left:158px;top:2px" width="36" height="42" viewBox="0 0 36 42"><path d="M30 3 34 7 12 33 6 36 8 30Z" fill="#5fb5e6" stroke="#2a6fa8" stroke-width="1.5"/><path d="M4 40h14" stroke="#2a6fa8" stroke-width="1.5"/></svg>
    <div class="th" style="left:25px;top:60px;grid-template-columns:117px 130px auto"><span>Request<br>No.</span><span>Requested<br>Date</span><span>Branch</span></div>
    <div class="td" style="left:25px;top:98px;grid-template-columns:117px 130px auto">
      <span><a href="#">56-0003</a></span><span>20/4/2013</span><span>GC1</span>
      <span><a href="#">56-0004</a></span><span>21/4/2013</span><span>GC2</span>
    </div>
    <div class="pager" style="left:300px;top:187px"><span>&lt;</span><b>1</b><span>2</span><span>3</span><span>4</span><span>&gt;</span></div>
  </section>

  <section class="abs panel" style="left:480px;top:375px;width:424px;height:218px">
    <h2 class="panel-title">My Working Requests</h2>
    <svg class="panel-icon" style="left:240px;top:4px" width="30" height="42" viewBox="0 0 30 42"><path d="M3 2h24M3 40h24" stroke="#1b4f8a" stroke-width="3"/><path d="M6 4c0 12 16 12 16 17S6 26 6 38h18c0-12-16-12-16-17S24 16 24 4Z" fill="#bfe6fa" stroke="#1b86c8" stroke-width="1.5"/><path d="M9 37c2-5 10-5 12 0Z" fill="#1b86c8"/></svg>
    <div class="th" style="left:24px;top:60px;grid-template-columns:117px 129px auto"><span>Request<br>No.</span><span>Requested<br>Date</span><span>Status</span></div>
    <div class="td" style="left:24px;top:98px;grid-template-columns:117px 129px auto">
      <span><a href="#">55-0200</a></span><span>25/3/2013</span><span>Waiting for progress</span>
      <span><a href="#">55-0210</a></span><span>24/3/2013</span><span>In progress</span>
      <span><a href="#">55-0300</a></span><span>18/3/2013</span><span>Incomplete document</span>
    </div>
    <div class="pager" style="left:303px;top:187px"><span>&lt;</span><b>1</b><span>2</span><span>3</span><span>4</span><span>&gt;</span></div>
  </section>

  <section class="abs panel" style="left:41px;top:610px;width:863px;height:157px">
    <h2 class="panel-title">Expiring Permits</h2>
    <svg class="panel-icon" style="left:179px;top:4px" width="42" height="42" viewBox="0 0 42 42"><circle cx="21" cy="21" r="19" fill="#e3212b" stroke="#a50f17" stroke-width="1.5"/><rect x="18" y="8" width="6" height="17" rx="3" fill="#fff"/><circle cx="21" cy="31" r="3.5" fill="#fff"/></svg>
    <div class="th" style="left:25px;top:51px;grid-template-columns:117px 130px 184px 99px 193px auto"><span>Permit No.</span><span>Expire Date</span><span>Permit Name</span><span>Branch</span><span>Required Time (Day)</span><span>Due Date</span></div>
    <div class="td" style="left:25px;top:79px;grid-template-columns:117px 130px 184px 99px 193px auto">
      <span><a href="#">AB56-0001</a></span><span>25/3/2013</span><span><a href="#">Permit Name ###10</a></span><span>GC1</span><span>30 <i class="flag is-red"></i></span><span>-40</span>
      <span><a href="#">BIO5502</a></span><span>24/3/2013</span><span><a href="#">Permit Name ###20</a></span><span>GC2</span><span>60 <i class="flag is-amber"></i></span><span>15</span>
    </div>
    <div class="pager" style="left:743px;top:124px"><span>&lt;</span><b>1</b><span>2</span><span>3</span><span>4</span><span>&gt;</span></div>
  </section>

  <section class="abs panel" style="left:41px;top:784px;width:424px;height:219px">
    <h2 class="panel-title">My In Progress Requests</h2>
    <svg class="panel-icon" style="left:263px;top:2px" width="46" height="46" viewBox="0 0 46 46"><rect x="6" y="4" width="26" height="34" fill="#d7eefb" stroke="#2a6fa8" stroke-width="1.5" transform="rotate(-8 19 21)"/><rect x="13" y="8" width="26" height="34" fill="#ffffff" stroke="#2a6fa8" stroke-width="1.5"/><path d="M18 16h16M18 21h16M18 26h16M18 31h12" stroke="#1b86c8" stroke-width="2"/></svg>
    <div class="th" style="left:22px;top:62px;grid-template-columns:116px 130px auto"><span>Request<br>No.</span><span>Requested<br>Date</span><span>Status</span></div>
    <div class="td" style="left:22px;top:101px;grid-template-columns:116px 130px auto">
      <span><a href="#">56-0001</a></span><span>24/4/2013</span><span>Waiting for progress</span>
      <span><a href="#">56-0002</a></span><span>21/4/2013</span><span>In progress</span>
    </div>
    <div class="pager" style="left:297px;top:188px"><span>&lt;</span><b>1</b><span>2</span><span>3</span><span>4</span><span>&gt;</span></div>
  </section>

  <div class="abs cta">New Requests</div>

  <section class="abs panel" style="left:480px;top:851px;width:424px;height:148px">
    <h2 class="panel-title">Recent Completed Requests</h2>
    <svg class="panel-icon" style="left:288px;top:2px" width="40" height="44" viewBox="0 0 40 44"><path d="M3 24 10 18 17 28 34 3 38 8 17 41Z" fill="#2aa0e4" stroke="#125a9a" stroke-width="1.5"/></svg>
    <div class="th" style="left:24px;top:56px;grid-template-columns:164px auto"><span>Request&nbsp; No.</span><span>Completed Date</span></div>
    <div class="td" style="left:24px;top:78px;grid-template-columns:164px auto;grid-auto-rows:19px">
      <span><a href="#">55-0100</a></span><span>25/3/2013</span>
      <span><a href="#">55-0088</a></span><span>24/3/2013</span>
    </div>
    <div class="pager" style="left:309px;top:121px"><span>&lt;</span><b>1</b><span>2</span><span>3</span><span>4</span><span>&gt;</span></div>
  </section>

  <aside class="abs faq">
    <div class="faq-inner">
      <h2 class="faq-title">Common<br>Questions</h2>
      <svg class="abs" style="left:140px;top:12px" width="80" height="80" viewBox="0 0 80 80"><circle cx="40" cy="40" r="30" fill="none" stroke="#ffffff" stroke-width="18"/><g fill="none" stroke="#e3212b" stroke-width="18" stroke-dasharray="23.56 23.56" transform="rotate(-20 40 40)"><circle cx="40" cy="40" r="30"/></g><circle cx="40" cy="40" r="39" fill="none" stroke="#c9ced6" stroke-width="1"/></svg>
      <ul class="faq-list">
        <li>Lorem ipsum dolor sit</li>
        <li>Pamet, consectetur</li>
        <li>Ladipisicing elit, sed do</li>
        <li>Heiusmod tempor</li>
        <li>Kincididunt ut labore et</li>
        <li>Adolore magna aliqua.</li>
        <li>Ut enim ad minim</li>
        <li>Veniam, quis nostrud e</li>
      </ul>
      <div class="faq-help">GET HELP</div>
    </div>
  </aside>
</main>

<footer>
  <div class="abs footer-band"></div>
  <div class="abs footer-media" role="img" aria-label="Illustration of a glowing blue chemical molecule structure">IMAGE GOES HERE</div>
  <div class="abs footer-text">Footer texts go here</div>
</footer>

</body>
</html>
```